Need a Modern WIX Website design

Need help designing a modern WIX website. I already started building on editor.SiteBuildr but I am not a designer and would like a more modern, update aesthetic look. This is not an e-commerce site. Just a website portraying our company, posting what products we offer, contact, about us, services. Logo is already on the editor.wix version with some content. Need a designer with vision, and ingenuity to set it apart change it a little and make it stand out. Please look at the current site for redesign and/or ideas https://corvadetradewks.sitebuildr.net/website
also need the design to be connected to our google domain www.ctw.supply

Please feel free to ask as many questions as possible

Target Market(s)

Tire repair shops, Tire stores, mechanic shops, tire replacement franchises, wheel and rim stores

Industry/Entity Type

we are wholesalers, B2B ..sell tire repair materials, tire hand tools, machinery, chemicals, wheel lug nuts, wheel accessories

Coding

Coded - Design and coding required

Number of Pages Required

5+ page

Font styles to use
Other font styles liked:
• Let designer choose

Colors

Designer to choose colors to be used in the design.

Requirements
Must have
• modern design layout, videos, high quality pictures, different ideas for pages (Home, shop, about, products, services, contact, faq, meet the team) translatable english to spanish
Nice to have
• would like to have an up to date modern look, interactive, easy to navigate,
Should not have
• not be hard to navigate for our customers

```html
<!DOCTYPE html>
<html lang="en">
<head>
<meta charset="utf-8">
<title>Corvade Trade Works</title>
<link href="https://fonts.googleapis.com/css2?family=Roboto:wght@400;500;700;900&display=swap" rel="stylesheet">
<style>
:root{
  --red:#d50f0f;
  --black:#0b0b0b;
  --dark:#151719;
  --white:#ffffff;
  --text:#333;
  --tile-shape:#e4e6e8;
}
*{margin:0;padding:0;box-sizing:border-box}
html,body{width:1200px;height:3722px;overflow:hidden}
body{position:relative;font-family:'Roboto',Arial,sans-serif;background:var(--white);color:var(--text)}
.abs{position:absolute}
.center{text-align:center;left:0;width:1200px}
/* header */
.site-header{position:absolute;top:0;left:0;width:1200px;height:101px;background:var(--black)}
.brand{left:162px;top:28px;display:flex;align-items:center;gap:12px;color:var(--white);font-weight:700;font-size:21px;letter-spacing:1px}
.brand-mark{width:38px;height:38px;border:3px solid var(--red)}
.call{right:165px;top:24px;font-size:11px;color:var(--white);font-weight:700;display:flex;align-items:center;gap:6px}
.call em{color:var(--red);font-style:normal}
.nav{top:67px;left:491px;display:flex;gap:25px;font-size:13px;color:var(--white)}
.nav span.active{color:var(--red);border-bottom:2px solid var(--red);padding-bottom:5px}
/* hero */
.hero{top:101px;left:0;width:1200px;height:469px;
  background:radial-gradient(ellipse 55% 75% at 62% 45%,#77777a 0%,#4e4e50 40%,transparent 75%),
             linear-gradient(90deg,#2a2a2a 0%,#3d3d3e 35%,#505052 60%,#2a2a2b 100%)}
.hero-kicker{top:258px;font-size:23px;font-weight:700;color:var(--red)}
.hero-title{top:281px;font-size:48px;font-weight:700;color:var(--white);letter-spacing:-1px}
.btn-red{background:var(--red);color:var(--white);border-radius:20px;font-size:13px;font-weight:700;display:flex;align-items:center;justify-content:center}
/* services */
.services{top:570px;left:0;width:1200px;height:423px;background:var(--black)}
.sec-title{font-weight:700}
.svc{width:260px;text-align:center;color:var(--white)}
.svc-icon{width:102px;height:102px;border:2px solid var(--red);border-radius:50%;margin:0 auto;display:flex;align-items:center;justify-content:center}
.svc h3{font-size:15px;font-weight:500;margin-top:22px}
.svc p{font-size:11px;line-height:15px;color:#ccc;margin:12px auto 0;width:240px;height:60px}
.btn-ghost{margin:18px auto 0;width:113px;height:34px;border:1.5px solid var(--white);border-radius:18px;font-size:10px;display:flex;align-items:center;justify-content:center}
.divider{width:1px;height:267px;top:679px;background:#444}
/* about */
.about-photo{top:993px;left:0;width:599px;height:515px;
  background:radial-gradient(ellipse 40% 35% at 35% 30%,#9a9a9c,transparent 70%),
             radial-gradient(ellipse 45% 45% at 70% 75%,#2f48b8,transparent 70%),
             linear-gradient(135deg,#3b3b3d 0%,#4a4a4e 40%,#2a3c8c 70%,#18255e 100%)}
.about-kicker{left:633px;top:1106px;font-size:29px;font-weight:700;color:var(--red)}
.about-title{left:633px;top:1134px;font-size:44px;font-weight:700;color:#1a1a1a;letter-spacing:-.5px}
.about-sub{left:635px;top:1182px;font-size:15px;color:#444}
.about-line{left:635px;top:1213px;width:44px;height:2px;background:#444}
.about-text{left:635px;top:1231px;width:396px;font-size:11.8px;line-height:17.2px;color:#555}
.btn-outline-red{left:635px;top:1374px;width:145px;height:43px;border:2px solid var(--red);border-radius:22px;color:var(--red);font-size:11px;display:flex;align-items:center;justify-content:center}
/* products */
.prod-img{top:1646px;width:288px;height:373px}
.prod{top:2044px;width:288px;text-align:center}
.prod h3{font-size:14px;font-weight:700;color:#222}
.prod p{font-size:10.5px;line-height:15px;color:#555;margin-top:8px;padding:0 22px}
/* testimonials */
.testimonials{top:2227px;left:0;width:1200px;height:433px;
  background:radial-gradient(ellipse 35% 45% at 30% 20%,#45474c,transparent 70%),
             radial-gradient(ellipse 40% 50% at 65% 30%,#3a3c41,transparent 70%),
             linear-gradient(180deg,#2a2c31,#1b1d21)}
.quote-mark{font-size:48px;font-weight:900;color:var(--red);line-height:1}
/* brands */
.tile{width:212px;height:202px;border:1px solid #bbb;background:var(--white);text-align:center}
.tile .shape{width:80px;height:80px;background:var(--tile-shape);border-radius:50%;margin:30px auto 0}
.tile span{display:block;margin-top:30px;font-size:12px;color:#444}
/* footer */
.footer{top:3268px;left:0;width:1200px;height:454px;background:var(--dark);color:var(--white)}
.hours{top:3331px;left:162px;width:874px;height:145px;background:var(--red);color:var(--white)}
.hours div{position:absolute;width:290px;text-align:center;top:44px}
.hours b{display:block;font-size:11px}
.hours strong{display:block;font-size:17px;margin-top:9px}
.social{width:29px;height:29px;border:1px solid var(--white);border-radius:50%}
.field{border:1px solid #666;font-size:10px;color:#aaa;padding:10px 12px;background:var(--dark)}
</style>
</head>
<body>
<header class="site-header">
  <div class="abs brand"><div class="brand-mark"></div>CORVADE TRADE WORKS</div>
  <div class="abs call">
    <svg width="16" height="16" viewBox="0 0 24 24" fill="none" stroke="#fff" stroke-width="2"><path d="M22 16.9v3a2 2 0 0 1-2.2 2 19.8 19.8 0 0 1-8.6-3.1 19.5 19.5 0 0 1-6-6A19.8 19.8 0 0 1 2.1 4.2 2 2 0 0 1 4.1 2h3a2 2 0 0 1 2 1.7c.1.9.4 1.8.7 2.7a2 2 0 0 1-.5 2.1L8 9.8a16 16 0 0 0 6 6l1.3-1.3a2 2 0 0 1 2.1-.4c.9.3 1.8.6 2.7.7a2 2 0 0 1 1.7 2z"/></svg>
    <span><em>Call Now -</em> 833-555-0182</span>
  </div>
  <nav class="abs nav"><span class="active">Home</span><span>About Us</span><span>Shop</span><span>Products</span><span>Services</span><span>Meet The Team</span><span>Faq</span><span>Contact</span></nav>
</header>

<section class="abs hero" role="img" aria-label="Close-up photo of a car tyre and alloy wheel"></section>
<div class="abs center hero-kicker">Your One Stop Tire Repair</div>
<h1 class="abs center hero-title">Supplier in New York</h1>
<div class="abs btn-red" style="left:533px;top:356px;width:133px;height:35px">Shop Now</div>

<section class="abs services"></section>
<h2 class="abs center sec-title" style="top:604px;font-size:26px;color:#fff">Services Offered</h2>
<div class="abs center" style="top:635px;font-size:12px;color:#ddd">Satisfying Our Clients</div>
<div class="abs divider" style="left:453px"></div>
<div class="abs divider" style="left:744px"></div>

<div class="abs svc" style="left:183px;top:684px">
  <div class="svc-icon">
    <svg width="54" height="54" viewBox="0 0 48 48" fill="none" stroke="#d50f0f" stroke-width="2.4" stroke-linecap="round">
      <path d="M9 26v-4a15 15 0 0 1 30 0v4"/>
      <rect x="6" y="24" width="7" height="11" rx="2" fill="#d50f0f"/>
      <rect x="35" y="24" width="7" height="11" rx="2" fill="#d50f0f"/>
      <path d="M38 35c0 4-4 6-10 6h-3"/>
      <circle cx="23" cy="41" r="2" fill="#d50f0f"/>
    </svg>
  </div>
  <h3>Stellar Customer Service</h3><p>For over 25 years, we have been providing excellent customer service by going the extra mile in making sure a customer is happy and satisfied with our company's...</p><div class="btn-ghost">LEARN MORE</div></div>

<div class="abs svc" style="left:469px;top:684px">
  <div class="svc-icon">
    <svg width="56" height="56" viewBox="0 0 48 48" fill="none" stroke="#d50f0f" stroke-width="2.4" stroke-linecap="round" stroke-linejoin="round">
      <path d="M24 4l4.5 3.3 5.5-.4 1.9 5.2 4.8 2.7-1.2 5.4 2.5 5-3.8 4 .2 5.6-5.3 1.6-2.8 4.8-5.2-1.8-5.2 1.8-2.8-4.8-5.3-1.6.2-5.6-3.8-4 2.5-5-1.2-5.4 4.8-2.7 1.9-5.2 5.5.4z"/>
      <circle cx="24" cy="24" r="11"/>
      <path d="M18.5 24.5l4 4 7.5-8"/>
    </svg>
  </div>
  <h3>High Quality Products</h3><p>Our products are trusted for their design &amp; engineering, &amp; we will continue to equip our customers with high-quality products and tools at the best value</p><div class="btn-ghost">LEARN MORE</div></div>

<div class="abs svc" style="left:760px;top:684px">
  <div class="svc-icon">
    <svg width="56" height="56" viewBox="0 0 48 48" fill="none" stroke="#d50f0f" stroke-width="2.4" stroke-linecap="round" stroke-linejoin="round">
      <circle cx="24" cy="12" r="7"/>
      <path d="M20.5 12l2.5 2.5 4.5-5"/>
      <rect x="5" y="30" width="5" height="12"/>
      <path d="M10 31l5-8h3v7h6v12H10"/>
      <rect x="38" y="30" width="5" height="12"/>
      <path d="M38 31l-5-8h-3v7"/>
      <path d="M24 42h14"/>
    </svg>
  </div>
  <h3>Commitment</h3><p>When a customer comes to us for parts it is often in the context of a long project. We offer Tire Alignment services that will help guide you throughout the course....</p><div class="btn-ghost">LEARN MORE</div></div>

<div class="abs about-photo" role="img" aria-label="Mechanic in blue overalls fitting a wheel with an impact wrench"></div>
<div class="abs about-kicker">Corvade Trade</div>
<h2 class="abs about-title">Works Inc</h2>
<div class="abs about-sub">Your One Stop Tire Repair Supplier in New York</div>
<div class="abs about-line"></div>
<p class="abs about-text">At Corvade Trade Works Inc we make sure to offer our clients the best Selection of tire repair products, tools and machinery as well as provide them with superb customer service. Our staff works with our customers to find exactly the right part they need for the right price. We're here to help inform you about our products, so that you only buy what is absolutely necessary for your establishment. Contact us today to learn more about what we do.</p>
<div class="abs btn-outline-red">LEARN MORE</div>

<h2 class="abs center sec-title" style="top:1566px;font-size:38px;color:#1a1a1a">Available Products</h2>
<div class="abs center" style="top:1610px;font-size:13px;color:#333">Supplying the Best Quality Merchandise</div>
<div class="abs prod-img" style="left:162px;background:radial-gradient(ellipse 50% 40% at 60% 72%,#a4a6ab,transparent 70%),linear-gradient(165deg,#1f2a45 0%,#2c3a62 45%,#4b4f58 100%)" role="img" aria-label="Technician handling a tyre and wheel"></div>
<div class="abs prod-img" style="left:456px;background:radial-gradient(ellipse 25% 18% at 75% 15%,#c2506e,transparent 70%),radial-gradient(ellipse 60% 50% at 45% 55%,#a9a7a4,transparent 75%),linear-gradient(160deg,#6e6c6a,#3a3a3a)" role="img" aria-label="Gloved hand on a brake disc"></div>
<div class="abs prod-img" style="left:752px;background:radial-gradient(ellipse 60% 35% at 30% 15%,#a59a4a,transparent 70%),radial-gradient(ellipse 30% 25% at 65% 35%,#d8d6cf,transparent 70%),linear-gradient(175deg,#4f4b35 0%,#262b38 50%,#1c2230 100%)" role="img" aria-label="Hands working in a car engine bay"></div>
<div class="abs prod" style="left:162px"><h3>Mufflers</h3><p>Your vehicle's performance requires top notch Mufflers to ensure your comfort and safety. You can trust us to supply you with only the best quality products in the market and guarantee your satisfaction. Get in touch with us today to see what else we can offer you, and stop by the store to purchase your Mufflers.</p></div>
<div class="abs prod" style="left:456px"><h3>Brake Pads</h3><p>Every vehicle operates best with well designed auto parts. That's why we carry a wide selection of parts and tools from several manufacturers — to ensure your vehicle is up and running at top performance in no time. Our variety of parts includes our top quality Brake Pads that come with different features.</p></div>
<div class="abs prod" style="left:752px"><h3>Windshield Wipers</h3><p>The most important thing your car needs is often also the most overlooked. We carry many different types of auto parts because we understand how vital they are to the overall performance of your vehicle. Our Windshield Wipers are some of our most popular items. Call us to see if we've got the brand you need in stock.</p></div>

<section class="abs testimonials" role="img" aria-label="Dark workshop photo background"></section>
<h2 class="abs center sec-title" style="top:2337px;font-size:34px;color:#fff">Testimonials</h2>
<div class="abs quote-mark" style="left:196px;top:2388px">&ldquo;</div>
<p class="abs" style="left:230px;top:2406px;width:740px;text-align:center;font-size:13px;line-height:18.5px;color:#ddd">Praesent congue quam et ligula tincidunt, id elementum leo tempor Ut sit amet condimentum felis. Etiam non lacus ac nisi tempor semper. Pellentesque euismod purus quis turpis accumsan, vitae aliquam elit porta. Ut pellentesque vestibulum lectus quis bibendum Sed varius nunc dui, quis consectetur tellus placerat eu. Praesent tincidunt lectus ut risus hendrerit, sed sollicitudin ligula faucibus. Nulla congue mi ut venenatis dictum sit amet condimentum</p>
<div class="abs quote-mark" style="left:882px;top:2482px">&rdquo;</div>
<div class="abs center" style="top:2510px;font-size:14px;font-weight:700;color:#fff">Dorian Vale</div>
<svg class="abs" style="left:580px;top:2556px" width="40" height="8"><circle cx="4" cy="4" r="2.5" fill="#d50f0f"/><circle cx="14" cy="4" r="2.5" fill="#fff"/><circle cx="24" cy="4" r="2.5" fill="#fff"/><circle cx="34" cy="4" r="2.5" fill="#fff"/></svg>

<h2 class="abs center sec-title" style="top:2717px;font-size:34px;color:#1a1a1a">Brands</h2>
<div class="abs center" style="top:2757px;font-size:12px;font-weight:500;color:#333">Who We Work With</div>
<div class="abs tile" style="left:162px;top:2794px"><div class="shape"></div><span>Vantor Patch Co</span></div>
<div class="abs tile" style="left:383px;top:2794px"><div class="shape"></div><span>Keelby Group</span></div>
<div class="abs tile" style="left:602px;top:2794px"><div class="shape"></div><span>Halden Works</span></div>
<div class="abs tile" style="left:823px;top:2794px"><div class="shape"></div><span>Brisk Lane Tools</span></div>
<div class="abs tile" style="left:162px;top:3005px"><div class="shape"></div><span>Ferro Bright</span></div>
<div class="abs tile" style="left:383px;top:3005px"><div class="shape"></div><span>Tessly</span></div>
<div class="abs tile" style="left:602px;top:3005px"><div class="shape"></div><span>Ridgepoint Weld</span></div>
<div class="abs tile" style="left:823px;top:3005px"><div class="shape"></div><span>Ironvale Tools</span></div>

<footer class="abs footer"></footer>
<div class="abs center" style="top:3305px;font-size:14px;font-weight:500;color:#fff">Working Hours</div>
<div class="abs hours">
  <div style="left:0"><b>Sunday - Monday</b><strong>Closed</strong></div>
  <div style="left:292px"><b>Tuesday - Friday</b><strong>10:00am - 7:00pm</strong></div>
  <div style="left:584px"><b>Saturday</b><strong>11:00am - 5:00pm</strong></div>
</div>
<div class="abs" style="left:204px;top:3504px;width:300px;text-align:center;color:#fff">
  <div style="font-size:16px;font-weight:500">Visit Us</div>
  <div style="font-size:11px;margin-top:10px">218 Harbor Line Avenue Oakdale, CA 94561</div>
  <div style="font-size:11px;margin-top:6px">corvadetradewks@mailbox.net &nbsp; | &nbsp; 833-555-0182</div>
</div>
<div class="abs social" style="left:292px;top:3580px"></div>
<div class="abs social" style="left:328px;top:3580px"></div>
<div class="abs social" style="left:364px;top:3580px"></div>
<div class="abs social" style="left:400px;top:3580px"></div>
<div class="abs" style="left:705px;top:3504px;width:252px;text-align:center;font-size:16px;font-weight:500;color:#fff">Contact Us</div>
<div class="abs field" style="left:705px;top:3529px;width:127px;height:28px;padding-top:8px">Name</div>
<div class="abs field" style="left:831px;top:3529px;width:126px;height:28px;padding-top:8px">Email</div>
<div class="abs field" style="left:705px;top:3556px;width:252px;height:34px">Type your message here...</div>
<div class="abs" style="left:705px;top:3589px;width:252px;height:32px;background:var(--red);color:#fff;font-size:12px;font-weight:700;display:flex;align-items:center;justify-content:center">Submit</div>
<div class="abs" style="left:0;top:3663px;width:1200px;height:1px;background:#333"></div>
<div class="abs center" style="top:3685px;font-size:10px;color:#999">©2022 by Corvade Trade Works Inc. Proudly created with SiteBuildr</div>
</body>
</html>
```